Simple, elegant, business card design required

Hi designers,I am looking for a simple yet elegant business card design.

Please make use of my logo (attached); you are free to tweak the logo should you wish to do so.

Our business is involved in many different fields - almost all of them involved in some form of "design", so that's really one of the key things I want to portray. I do not wish to specify which field of design, exactly.

I prefer white on black (or just monochromatic), but if you have a different, creative idea, I am open to that too.

You can use artsy photographs provided that you have the license to use those. Please feel free to ask me any questions.
Updates

Project Deadline Extended Reason: Small extension for potential revisions. Did not get the time to provide as much feedback as I can. Added Wednesday, July 09, 2014

Target Market(s)

High-end customers looking for design consultancy

Industry/Entity Type

Business

Contact Information for Business Card

Name: Gareth Moonfield
Position: Creative Director
Mobile: +155603928174
Address: Barrow Lane, Ashcombe upon Teme, Harrowshire GL12 4RT
Website: torvakest.com (not launched yet)

Requirements
Must have
• Design layout must be clean, original, and text must be readable when printed.
Should not have
• ~ No business card templates please. Anyone using this will be reported.
• ~ Please don't spam entries.

```html
<!DOCTYPE html>
<html lang="en">
<head>
<meta charset="utf-8">
<title>Torvakest – Business Card</title>
<link rel="stylesheet" href="https://fonts.googleapis.com/css2?family=Open+Sans:wght@400;600;700&display=swap">
<style>
  :root {
    --backdrop: #2a0c0c;
    --card-white: #ffffff;
    --card-black: #0b0b0c;
    --card-black-soft: #1c1d1f;
    --silver-light: #f2f2f2;
    --silver-mid: #a9a9ab;
    --silver-dark: #6d6d70;
    --text-light: #f4f4f4;
    --text-muted: #8a8a8c;
    --icon-bg: #7a7a7c;
  }
  * { margin: 0; padding: 0; box-sizing: border-box; }
  html, body {
    width: 1200px; height: 800px; overflow: hidden;
    background: var(--backdrop);
    font-family: "Open Sans", Arial, sans-serif;
  }
  .business-card {
    position: absolute; left: 120px; top: 126px;
    width: 960px; height: 548px;
    background: var(--card-white);
    box-shadow: 0 20px 40px rgba(0,0,0,0.5);
    overflow: hidden;
  }
  .card-shapes { position: absolute; inset: 0; }
  .brand-name {
    position: absolute; left: 352px; top: 96px;
    font-size: 34px; font-weight: 600; letter-spacing: 10px;
    line-height: 1;
    color: var(--card-black);
  }
  .holder { position: absolute; left: 55px; top: 282px; }
  .holder-name { font-size: 24px; font-weight: 700; color: var(--text-light); line-height: 1.1; }
  .holder-role { font-size: 15px; color: var(--text-muted); margin-top: 2px; }
  .contact-list { position: absolute; left: 55px; top: 360px; list-style: none; }
  .contact-item {
    display: flex; align-items: flex-start; gap: 10px;
    font-size: 20px; color: var(--text-light); line-height: 26px;
  }
  .contact-item + .contact-item { margin-top: 2px; }
  .contact-item.web { margin-top: 12px; }
  .contact-icon { width: 22px; height: 22px; margin-top: 2px; flex: none; }
</style>
</head>
<body>
  <div class="business-card">
    <svg class="card-shapes" width="960" height="548" viewBox="0 0 960 548">
      <defs>
        <linearGradient id="silver" x1="0" y1="0" x2="1" y2="0">
          <stop offset="0" stop-color="var(--silver-dark)"/>
          <stop offset="0.45" stop-color="var(--silver-light)"/>
          <stop offset="0.7" stop-color="var(--silver-mid)"/>
          <stop offset="1" stop-color="var(--silver-dark)"/>
        </linearGradient>
        <linearGradient id="darkPanel" x1="0" y1="0" x2="1" y2="1">
          <stop offset="0" stop-color="var(--card-black-soft)"/>
          <stop offset="1" stop-color="var(--card-black)"/>
        </linearGradient>
      </defs>
      <polygon class="dark-panel" points="0,262 960,212 960,548 0,548" fill="url(#darkPanel)"/>
      <polygon class="silver-strip" points="0,252 960,202 960,214 0,264" fill="url(#silver)"/>
      <rect class="brand-block" x="55" y="60" width="265" height="150" fill="var(--card-black)"/>
    </svg>

    <div class="brand-name">TORVAKEST</div>

    <div class="holder">
      <div class="holder-name">Gareth Moonfield</div>
      <div class="holder-role">Creative Director</div>
    </div>

    <ul class="contact-list">
      <li class="contact-item phone">
        <svg class="contact-icon" viewBox="0 0 20 20" aria-hidden="true">
          <rect width="20" height="20" rx="2" fill="var(--icon-bg)"/>
          <rect x="6" y="3" width="8" height="14" rx="1.5" fill="none" stroke="#fff" stroke-width="1.5"/>
          <circle cx="10" cy="14.5" r="0.9" fill="#fff"/>
        </svg>
        <span>+155603928174</span>
      </li>
      <li class="contact-item address">
        <svg class="contact-icon" viewBox="0 0 20 20" aria-hidden="true">
          <rect width="20" height="20" rx="2" fill="var(--icon-bg)"/>
          <path d="M3 10 L10 4 L17 10 M5.5 9 V16 H14.5 V9" fill="none" stroke="#fff" stroke-width="1.6"/>
          <rect x="8.5" y="11.5" width="3" height="4.5" fill="#fff"/>
        </svg>
        <span>Barrow Lane, Ashcombe upon Teme<br>Harrowshire GL12 4RT</span>
      </li>
      <li class="contact-item web">
        <svg class="contact-icon" viewBox="0 0 20 20" aria-hidden="true">
          <rect width="20" height="20" rx="2" fill="var(--icon-bg)"/>
          <circle cx="10" cy="10" r="6" fill="none" stroke="#fff" stroke-width="1.3"/>
          <ellipse cx="10" cy="10" rx="2.6" ry="6" fill="none" stroke="#fff" stroke-width="1"/>
          <path d="M4 10 H16 M5 7 H15 M5 13 H15" stroke="#fff" stroke-width="1"/>
        </svg>
        <span>torvakest.com</span>
      </li>
    </ul>
  </div>
</body>
</html>
```